KBRF website design

We need a page template website design for a cms website. Please see the brief attached for the details.
The client is the Kestrel Brook Ramfold Federation which is an organisation promoting the White Suffolk Sheep Breed within Australia.
Updates

Reason: So that my top few designs can make changes and re-submit.

Target Market(s)

See attached brief

```html
<!DOCTYPE html>
<html lang="en">
<head>
<meta charset="utf-8">
<title>Kestrel Brook Ramfold Federation</title>
<link href="https://fonts.googleapis.com/css2?family=Arimo:wght@400;700&display=swap" rel="stylesheet">
<style>
:root{
  --green:#0e9446;
  --green-dark:#0b6b33;
  --pale:#e6f6dc;
  --ink:#333;
  --muted:#8a8a8a;
  --line:#d8d8d8;
  --panel:#f2f1f1;
  --dark:#3a3a3a;
  --footer:#1c1c1c;
  --gold:#f2c200;
}
*{margin:0;padding:0;box-sizing:border-box}
html,body{width:1200px;height:1181px;overflow:hidden;background:#fff;font-family:"Arimo",Arial,sans-serif;color:var(--ink)}
.canvas{position:relative;width:1200px;height:1181px}
.abs{position:absolute}
.band{left:0;top:273px;width:1200px;height:706px;background:linear-gradient(135deg,#eef9e6,#dff3d3 50%,#ecf8e4)}
.footer{left:0;top:979px;width:1200px;height:202px;background:var(--footer)}
.brand{display:flex;align-items:center;gap:10px;font-size:22px;font-weight:700;color:var(--green-dark)}
.brand i{display:block;width:30px;height:30px;background:var(--green)}
.site-title{left:464px;top:56px;font-size:19px;color:#555}
.nav-rule{left:256px;top:125px;width:721px;height:1px;background:var(--line)}
.nav{left:256px;top:138px;width:721px;display:flex;font-size:9.5px;color:#666}
.nav span{flex:1;text-align:center}
.nav .active{color:var(--green)}
.nav-bar{left:284px;top:156px;width:37px;height:3px;background:var(--green)}
.sheet{left:256px;top:159px;width:721px;height:852px;background:#fff;border:1px solid #e6e6e6;border-top:0}
.hero{left:283px;top:188px;width:664px;height:245px;background:linear-gradient(180deg,#7b9a6c 0%,#5d7f3f 40%,#6f9a3c 70%,#5f8a2e 100%)}
.arrow{top:300px;font-size:18px;color:#fff}
.rule{left:283px;top:446px;width:664px;height:1px;background:var(--line)}
.side{left:759px;top:449px;width:188px;height:530px;background:var(--panel)}
h1{left:284px;top:467px;font-size:17px;font-weight:400;color:#333}
.copy{left:284px;width:430px;font-size:8px;line-height:11px;color:var(--muted)}
.copy b{color:#333}
.aims{left:284px;top:586px;width:440px;list-style:none;font-size:8px;color:var(--muted)}
.aims li{position:relative;padding-left:16px;line-height:15px;margin-bottom:5px}
.aims li:before{content:"";position:absolute;left:1px;top:5px;width:5px;height:5px;border-radius:50%;background:#ccc}
.conf{left:283px;top:737px;width:446px;height:87px;background:var(--dark);color:#fff}
.conf h2{position:absolute;left:26px;top:10px;font-size:15px;font-weight:400}
.conf h2 small{font-size:9px;color:#ccc;margin-left:6px}
.conf p{position:absolute;left:26px;top:35px;font-size:8px;color:#bbb}
.conf .links{position:absolute;left:26px;top:58px;font-size:8.5px;color:#ddd;display:flex;gap:14px}
.conf .links .on{color:var(--gold);text-decoration:underline}
.ribbon{left:667px;top:737px}
.card{left:792px;width:127px;background:#fff}
.card .pic{height:95px}
.card .cap{height:29px;display:flex;align-items:center;gap:8px;padding-left:11px;font-size:9.5px;color:#555}
.card .cap.on{background:var(--green);color:#fff;font-weight:700}
.btn{left:792px;width:123px;height:30px;background:linear-gradient(#444,#2a2a2a);border-radius:2px;color:#fff;font-size:8.5px;display:flex;align-items:center;padding-left:9px}
.btn em{position:absolute;right:0;top:0;width:33px;height:30px;border-left:1px solid #222;display:flex;align-items:center;justify-content:center}
.btn em span{width:13px;height:13px;border-radius:50%;border:1px solid #555;font-style:normal;font-size:8px;color:#aaa;display:flex;align-items:center;justify-content:center}
.lorem{left:284px;top:856px;width:440px;font-size:8px;line-height:11px;color:var(--muted)}
.f-head{top:1041px;font-size:10.5px;color:#ddd}
.f-list{left:517px;top:1065px;list-style:none;font-size:8px;color:#999}
.f-list li{line-height:14.5px}
.f-list .on{color:var(--green);text-decoration:underline}
.office{left:657px;top:1066px;font-size:8px;line-height:14.5px;color:#999}
.office b{color:#bbb}
.social{top:1068px;width:26px;height:26px;border-radius:50%}
.legal{left:256px;top:1129px;font-size:8.5px;line-height:14px;color:#ccc}
.legal u{color:var(--green);font-weight:700}
</style>
</head>
<body>
<div class="canvas">
  <div class="abs band"></div>
  <div class="abs footer"></div>

  <div class="abs brand" style="left:258px;top:48px"><i></i>Kestrel Brook</div>
  <div class="abs site-title">Kestrel Brook Ramfold Federation</div>

  <div class="abs nav-rule"></div>
  <div class="abs sheet"></div>
  <nav class="abs nav">
    <span class="active">Home</span><span>About</span><span>Search</span><span>Member Services</span><span>Stud Pages</span><span>News</span><span>Sales</span><span>Links</span><span>Contact</span>
  </nav>
  <div class="abs nav-bar"></div>

  <div class="abs hero" role="img" aria-label="Flock of white sheep grazing in a green paddock with trees and hills behind"></div>
  <div class="abs arrow" style="left:298px">&#8249;</div>
  <div class="abs arrow" style="left:918px;color:var(--gold)">&#8250;</div>

  <div class="abs rule"></div>
  <div class="abs side"></div>

  <h1 class="abs">Welcome to our website</h1>
  <p class="abs copy" style="top:499px">The White Suffolk is an Australian breed developed for Australian conditions. The White Suffolk is proving to be the ideal prime lamb terminal sire in wide-ranging areas and environments of Australia.</p>
  <p class="abs copy" style="top:527px">It is giving outstanding results in the dry, arid, pastoral zones; all types of agricultural, mixed farming areas; and also in higher rainfall districts.</p>
  <p class="abs copy" style="top:557px">The <b>KESTREL BROOK RAMFOLD FEDERATION</b> aims to:</p>
  <ul class="abs aims">
    <li>be at the forefront of marketing and promotion of the White Suffolk breed</li>
    <li>better educate our members and commerical breeders on providing superior genetics to the Australian lamb industry</li>
    <li>continue to develop the White Suffolk breed to the advantage of all involved in the Australian lamb industry</li>
    <li>encourage extensive use of genetic evaluation and continue to benchmark the White Suffolk breed to<br>become the leading performance breed</li>
    <li>remain at the forefront of recent technological advances within the livestock industry</li>
    <li>promote the White Suffolk as an alternative maternal sire</li>
  </ul>

  <section class="abs conf">
    <h2>KBRF National Conference <small>- held Feb 16th - 19th 2014</small></h2>
    <p>Check out all the news from conference :</p>
    <div class="links"><span class="on">Media Releases</span><span>|</span><span>Powerpoint presentations</span><span>|</span><span>Photo Gallery</span></div>
  </section>
  <svg class="abs ribbon" width="40" height="38" viewBox="0 0 40 38"><path d="M0 0H40V38L20 26L0 38Z" fill="var(--green)"/></svg>

  <p class="abs lorem">Lorem ipsum dolor sit amet, consectetur adipisicing elit, sed do eiusmod tempor incididunt ut labore et dolore magna aliqua. Ut enim ad minim veniam, quis nostrud exercitation ullamco laboris nisi ut aliquip ex ea commodo consequat.</p>

  <div class="abs card" style="top:482px">
    <div class="pic" role="img" aria-label="Close view of a white sheep's fleece" style="background:linear-gradient(135deg,#d9d2c4,#b8ad98)"></div>
    <div class="cap"><svg width="12" height="12" viewBox="0 0 12 12"><circle cx="6" cy="6" r="5" fill="none" stroke="var(--green)"/><text x="6" y="9" font-size="8" text-anchor="middle" fill="var(--green)">?</text></svg>Prime Lamb Helpline</div>
  </div>
  <div class="abs card" style="top:615px">
    <div class="pic" role="img" aria-label="Calendar page with pins marking dates" style="background:linear-gradient(135deg,#e4eeee,#b9cfcf)"></div>
    <div class="cap on"><svg width="12" height="11" viewBox="0 0 12 11"><rect x="0.5" y="1.5" width="11" height="9" fill="none" stroke="#fff"/><path d="M0.5 4H11.5M3 6H9M3 8H9" stroke="#fff"/></svg>Events</div>
  </div>
  <div class="abs card" style="top:745px">
    <div class="pic" role="img" aria-label="Typewritten newsflash on paper" style="background:linear-gradient(135deg,#dfe8f0,#a9b8c6)"></div>
    <div class="cap"><svg width="12" height="12" viewBox="0 0 12 12"><rect x="1" y="1" width="10" height="10" fill="none" stroke="var(--green)"/><path d="M3 4H9M3 6H9M3 8H7" stroke="var(--green)"/></svg>Latest News</div>
  </div>

  <div class="abs btn" style="top:884px">Members Resources<em><span>&#8250;</span></em></div>
  <div class="abs btn" style="top:921px">Web Manager Login<em><span>&#8250;</span></em></div>

  <div class="abs brand" style="left:258px;top:1068px"><i></i>Kestrel Brook</div>
  <div class="abs legal">Copyright Kestrel Brook Ramfold Federation<br>Website design and development by <u>Pixelfern</u></div>

  <div class="abs f-head" style="left:517px">Site Links</div>
  <ul class="abs f-list">
    <li class="on">Home</li><li>About</li><li>Search</li><li>Member Services</li><li>Stud Pages</li><li>Sales</li><li>Contact</li>
  </ul>

  <div class="abs f-head" style="left:657px">Office Location</div>
  <div class="abs office"><b>Secretary: Mara Lindqvist</b><br>PO Box 214, Elmvale, SA 5990<br>Phone (08) 5550 1234 Fax (08) 5550 4321</div>

  <div class="abs f-head" style="left:836px">Follow Us</div>
  <div class="abs social" style="left:835px;background:#3b5a99"></div>
  <div class="abs social" style="left:868px;background:#3fa6dd"></div>
</div>
</body>
</html>
```